Business card for Full Stable Care Vandorpe

I would like to have me designed an professional business card with my existing logo for my company called : full stable care vandorpe gcv.
I prefer a two sided business card with on the back side only the horses head and the website : fscvandorpe-example.eu
Only one colour shouldbe all right.
The logo must appear in a nic professional way on the business card.

Other suggestion are welcome.

All copy wrights must be released by the designer after we have selected a final design.

Target Market(s)

Equestrian businesses

Industry/Entity Type

Business

Contact Information for Business Card

Laurent Vandorpe
Title: zaakvoerder
Full Stable Care Vandorpe GCV
Molkenweg 47
B - 2820 Bonheiden
België
Phone: + 32 491 68 27 04
Mail: laurent@fscvandorpe-example.eu

Font styles to use
Serif

Requirements
Must have
• My own logo
• See attached files
• Website: fscvandorpe-example.eu

```html
<!DOCTYPE html>
<html lang="nl">
<head>
<meta charset="utf-8">
<title>Full Stable Care Vandorpe – business card</title>
<link rel="stylesheet" href="https://fonts.googleapis.com/css2?family=PT+Serif:wght@400;700&display=swap">
<style>
  :root {
    --backdrop: #3b3b3b;
    --card: #ffffff;
    --ink: #1e1e1e;
    --ink-soft: #4a4a4a;
    --decor: #e6e6e6;
  }
  * { box-sizing: border-box; margin: 0; padding: 0; }
  html, body { width: 1105px; height: 1200px; overflow: hidden; }
  body {
    background: var(--backdrop);
    font-family: "PT Serif", Georgia, serif;
    color: var(--ink);
    position: relative;
  }
  .card {
    position: absolute;
    left: 196px;
    width: 720px;
    height: 410px;
    background: var(--card);
    overflow: hidden;
  }
  .card--front { top: 146px; }
  .card--back { top: 602px; }

  .decor-area {
    position: absolute;
    background: radial-gradient(ellipse at center, var(--decor) 0%, rgba(230,230,230,0.6) 45%, rgba(255,255,255,0) 72%);
  }
  .card--front .decor-area { left: 0; top: -20px; width: 420px; height: 450px; }
  .card--back .decor-area { left: 120px; top: -10px; width: 520px; height: 440px; }

  .wordmark {
    position: absolute;
    display: flex;
    align-items: center;
    gap: 10px;
    font-weight: 700;
    color: var(--ink);
    white-space: nowrap;
  }
  .wordmark__dot {
    width: 14px; height: 14px;
    border-radius: 50%;
    background: var(--ink);
    flex: none;
  }
  .card--front .wordmark { right: 36px; top: 52px; font-size: 24px; }
  .card--back .wordmark {
    left: 0; right: 0; top: 200px;
    justify-content: center;
    font-size: 34px;
  }

  .holder-name {
    position: absolute;
    left: 43px; top: 208px;
    font-size: 26px;
    font-weight: 700;
  }
  .address {
    position: absolute;
    left: 43px; top: 278px;
    font-size: 20px;
    line-height: 26px;
    color: var(--ink-soft);
    font-style: normal;
  }
  .contact {
    position: absolute;
    right: 36px; top: 298px;
    list-style: none;
    font-size: 19px;
    line-height: 27px;
    color: var(--ink-soft);
    text-align: right;
  }
  .contact li { display: flex; align-items: center; justify-content: flex-end; gap: 10px; }
  .contact svg { width: 17px; height: 17px; fill: var(--ink); flex: none; }

  .website {
    position: absolute;
    left: 0; right: 0; top: 276px;
    text-align: center;
    font-size: 19px;
    letter-spacing: 0.55em;
    color: var(--ink-soft);
  }
</style>
</head>
<body>

<section class="card card--front" aria-label="Front of business card">
  <div class="decor-area" role="img" aria-label="Large faint company emblem as background decoration"></div>
  <div class="wordmark"><span class="wordmark__dot"></span>Full Stable Care Vandorpe</div>

  <h1 class="holder-name">Laurent Vandorpe</h1>
  <address class="address">
    Full Stable Care<br>
    Vandorpe GCV<br>
    Molkenweg 47<br>
    B - 2870 Heidebeek, België
  </address>

  <ul class="contact">
    <li>+ 32 491 68 27 04
      <svg viewBox="0 0 24 24" aria-hidden="true"><path d="M6.6 10.8a15.1 15.1 0 0 0 6.6 6.6l2.2-2.2a1 1 0 0 1 1-.25 11.4 11.4 0 0 0 3.6.57 1 1 0 0 1 1 1V20a1 1 0 0 1-1 1A17 17 0 0 1 3 4a1 1 0 0 1 1-1h3.5a1 1 0 0 1 1 1c0 1.25.2 2.45.57 3.57a1 1 0 0 1-.25 1z"/></svg>
    </li>
    <li>laurent@fscvandorpe-example.eu
      <svg viewBox="0 0 24 24" aria-hidden="true"><path d="M2 5h20v2l-10 7L2 7z"/><path d="M2 9l10 7 10-7v10H2z"/></svg>
    </li>
    <li>fscvandorpe-example.eu
      <svg viewBox="0 0 24 24" aria-hidden="true"><circle cx="12" cy="12" r="10"/><path d="M2 12h20M12 2c3 3 3 17 0 20M12 2c-3 3-3 17 0 20" fill="none" stroke="#fff" stroke-width="1.4"/></svg>
    </li>
  </ul>
</section>

<section class="card card--back" aria-label="Back of business card">
  <div class="decor-area" role="img" aria-label="Large faint company emblem as background decoration"></div>
  <div class="wordmark"><span class="wordmark__dot"></span>Full Stable Care Vandorpe</div>
  <p class="website">fscvandorpe-example.eu</p>
</section>

</body>
</html>
```